A Better Way to Celebrate

Bramblecast is a party invitation service with a charity twist. Users can send party invitations to guests, giving them the option to contribute money instead of bring a gift. All money contributed is pooled and split between getting a special present from all, and giving to a local charity.

Bramblecast tagline is “One for you, one for charity”

The target audience are people involved in: kids birthdays, farewell/leaving parties, baby showers, adult birthday parties, teacher gifts,

- an easy way to give to charity
- get the gift you really want. And get less gifts, so no issues with trying to store things you don’t need or won’t get played with
- eco friendly, reduces the need for paper. Less gifts mean less garbage to be thrown away
- saves guests the hassle of shopping, saves time
- easy way to manage your party. The Host Panel tracks all RSVPs, contributions and can send thank you cards (similar to okura and lanternwick).

We would like to have a catchy, exciting fun yet elegant double sided flyer with emphasis on clear communication of the Bramblecas concept (get the gift you really want, give some back to a local charity) and the above listed benefits.

The front page should ideally have one or a few inspirational images and the back side should be more descriptional. Please visit our website: bramblecast-invites.example for more details.

It should fit half an A4 page.

Reason: We still haven't decided on the final design.

Target Market(s)

Children, Adults (farewell parties, anniversaries, birthdays, baby showers)

Our website is mainly kids oriented at the moment but we would like to include the above target audience as well.

Industry/Entity Type

Communication

Requirements
Must have
• Get one big gift you really want (instead of piles of un-needed gifts) and give some back to charity.

Must show that Bramblecast can be a great tool for managing the invitation process (sending the online invitations, tracking the rsvps, sending reminders and thank you mails as well as tracking payments for a pooled gift. (ie. knowing who contributed online to a pooled gift, so no more hassle of reminding people to bring money and manually track who contributed and who didn't)

```html
<!DOCTYPE html>
<html lang="en">
<head>
<meta charset="utf-8">
<title>Bramblecast – A Better Way to Celebrate</title>
<link rel="stylesheet" href="https://fonts.googleapis.com/css2?family=Open+Sans:wght@300;400;600;700;800&family=Nunito:wght@900&family=Titan+One&display=swap">
<style>
  :root {
    --stage: #ecebe8;
    --paper: #ffffff;
    --pink: #e6007e;
    --pink-soft: #ef4f9c;
    --pink-wash: #fbe3ef;
    --green: #6cc13a;
    --green-dark: #4e9a22;
    --ink: #1e1e1e;
    --ink-soft: #3a3a3a;
    --red-arrow: #8a1230;
    --sky: #3fb6e6;
  }
  * { box-sizing: border-box; margin: 0; padding: 0; }
  html, body { width: 1200px; height: 848px; overflow: hidden; }
  body {
    background: var(--stage);
    font-family: "Open Sans", Arial, sans-serif;
    color: var(--ink);
    position: relative;
  }
  .page {
    position: absolute;
    top: 42px;
    width: 538px;
    height: 763px;
    background: var(--paper);
    overflow: hidden;
    box-shadow: 0 2px 8px rgba(0,0,0,.18);
  }
  .page--front { left: 52px; background: linear-gradient(180deg, var(--pink-wash) 0%, #ffffff 42%); }
  .page--back { left: 612px; }
  .abs { position: absolute; }

  /* Brand */
  .brand { display: flex; align-items: center; gap: 8px; }
  .brand__mark { width: 30px; height: 30px; background: var(--pink); border-radius: 4px; }
  .brand__name { font-weight: 600; font-size: 34px; color: var(--ink); letter-spacing: -0.5px; line-height: 1; }
  .brand__tagline { font-size: 13px; color: var(--ink-soft); }

  /* Front */
  .bunting { left: 0; top: 0; width: 320px; height: 36px;
    background: linear-gradient(90deg, #7fcf4a, #2fa9e0, #e6007e, #8d4fc2, #ffb400, #2fa9e0, #e6007e); opacity: .85; }
  .balloons { left: 320px; top: 0; width: 218px; height: 150px;
    background: radial-gradient(circle at 30% 45%, #e5157f 0 22%, transparent 23%),
                radial-gradient(circle at 58% 30%, #9b3fd0 0 24%, transparent 25%),
                radial-gradient(circle at 72% 68%, #8ccf3e 0 22%, transparent 23%),
                radial-gradient(circle at 90% 35%, #2fa5df 0 22%, transparent 23%),
                transparent; }
  .front-brand { left: 43px; top: 58px; }
  .front-tagline { left: 86px; top: 108px; }
  .headline { left: 0; width: 538px; top: 150px; text-align: center;
    font-weight: 300; font-size: 50px; line-height: 56px; color: var(--ink); }
  .subhead { left: 0; width: 538px; top: 272px; text-align: center;
    font-family: "Nunito", Arial, sans-serif; font-weight: 900; font-size: 19px; color: var(--pink); }
  .gifts { left: 30px; top: 305px; width: 480px; height: 320px; border-radius: 6px;
    background: radial-gradient(ellipse at 45% 55%, #ffffff 0%, #f3eef0 55%, #e7d6dc 100%); }
  .gifts::after { content: ""; position: absolute; left: 40%; top: 0; width: 8%; height: 100%;
    background: linear-gradient(180deg, #d41f2a, #a3121c); opacity: .35; }
  .benefits { left: 40px; top: 642px; width: 470px;
    display: grid; grid-template-columns: 238px 232px; row-gap: 6px; font-size: 12.5px; line-height: 15px; color: var(--ink-soft); }
  .benefits ul { list-style: none; display: flex; flex-direction: column; gap: 6px; }
  .benefits li { display: flex; gap: 7px; }
  .check { flex: 0 0 14px; width: 14px; height: 14px; margin-top: 1px; }

  /* Back */
  .photo { left: 0; top: 0; width: 538px; height: 248px;
    background: linear-gradient(180deg, #c9b2a6 0%, #d9a3a3 45%, #f1c0d6 80%, #ffffff 100%); }
  .how { left: 46px; top: 220px; font-family: "Titan One", Arial, sans-serif; font-size: 25px;
    color: var(--green); font-style: italic; letter-spacing: .5px;
    text-shadow: 0 0 0 #fff, 1px 1px 0 #fff, -1px -1px 0 #fff; }
  .steps-icons { left: 0; top: 258px; width: 538px; height: 70px; }
  .how-col { top: 330px; font-size: 11.5px; font-weight: 700; line-height: 14px; color: var(--ink-soft); }
  .how-col ul { list-style: none; display: flex; flex-direction: column; gap: 8px; }
  .how-col li { position: relative; padding-left: 14px; }
  .how-col li::before { content: ""; position: absolute; left: 0; top: 4px; width: 6px; height: 6px; background: var(--pink); }
  .how-col--1 { left: 50px; width: 120px; }
  .how-col--2 { left: 186px; width: 150px; }
  .how-col--3 { left: 354px; width: 160px; }

  .steps-box { left: 41px; top: 430px; width: 452px; height: 236px; background: var(--pink-soft);
    border-radius: 12px; padding: 20px 20px 0 22px; color: #fff; }
  .steps-tab { left: 64px; top: 408px; width: 204px; height: 30px; background: var(--green);
    border: 2px solid #fff; border-radius: 15px; text-align: center;
    font-family: "Titan One", Arial, sans-serif; font-style: italic; font-size: 18px; line-height: 26px; color: #fff; letter-spacing: .5px; }
  .steps { list-style: none; font-weight: 600; font-size: 14.5px; line-height: 18px; }
  .steps li { display: flex; margin-bottom: 4px; }
  .steps b { flex: 0 0 62px; font-weight: 600; white-space: nowrap; }
  .steps span { padding-left: 9px; }
  .steps-cta { position: absolute; left: 0; right: 0; bottom: 8px; text-align: center;
    font-weight: 700; font-size: 19px; letter-spacing: .6px; }
  .back-brand { left: 0; width: 538px; top: 688px; justify-content: center; }
  .back-brand .brand__name { font-size: 28px; }
  .back-brand .brand__mark { width: 24px; height: 24px; }
  .footer { left: 0; width: 538px; top: 732px; text-align: center; font-size: 13.5px; color: var(--ink); }
  .footer b { font-weight: 700; }
  .footer .divider { display: inline-block; width: 1px; height: 16px; background: #999; vertical-align: middle; margin: 0 6px; }
  .footer .social { display: inline-block; width: 12px; height: 12px; background: #4c6aa8; vertical-align: -1px; margin-right: 4px; }
</style>
</head>
<body>

<section class="page page--front">
  <div class="abs bunting" role="img" aria-label="Colourful party bunting flags"></div>
  <div class="abs balloons" role="img" aria-label="Bunch of colourful party balloons"></div>

  <div class="abs brand front-brand">
    <span class="brand__mark"></span>
    <span class="brand__name">bramblecast</span>
  </div>
  <p class="abs brand__tagline front-tagline">one for you, one for charity</p>

  <h1 class="abs headline">A Better Way to<br>Celebrate</h1>
  <p class="abs subhead">Get the gift you want and give a little back</p>

  <div class="abs gifts" role="img" aria-label="Two white gift boxes with red ribbons tagged You and Charity, with confetti"></div>

  <div class="abs benefits">
    <ul>
      <li><svg class="check" viewBox="0 0 14 14"><circle cx="7" cy="7" r="7" fill="#ffb400"/><path d="M3.5 7.2l2.4 2.3 4.6-4.8" stroke="#e6007e" stroke-width="2" fill="none"/></svg>Get the gift your really want and support a local charity</li>
      <li><svg class="check" viewBox="0 0 14 14"><circle cx="7" cy="7" r="7" fill="#ffb400"/><path d="M3.5 7.2l2.4 2.3 4.6-4.8" stroke="#e6007e" stroke-width="2" fill="none"/></svg>Teach your child the fun of sharing</li>
      <li><svg class="check" viewBox="0 0 14 14"><circle cx="7" cy="7" r="7" fill="#ffb400"/><path d="M3.5 7.2l2.4 2.3 4.6-4.8" stroke="#e6007e" stroke-width="2" fill="none"/></svg>Save guests the hassle of shopping</li>
    </ul>
    <ul>
      <li><svg class="check" viewBox="0 0 14 14"><circle cx="7" cy="7" r="7" fill="#ffb400"/><path d="M3.5 7.2l2.4 2.3 4.6-4.8" stroke="#e6007e" stroke-width="2" fill="none"/></svg>Reduce waste generated from packaging and wrapping</li>
      <li><svg class="check" viewBox="0 0 14 14"><circle cx="7" cy="7" r="7" fill="#ffb400"/><path d="M3.5 7.2l2.4 2.3 4.6-4.8" stroke="#e6007e" stroke-width="2" fill="none"/></svg>Manage your party, seamlessly track RSVPs and contributions and send thank you cards</li>
    </ul>
  </div>
</section>

<section class="page page--back">
  <div class="abs photo" role="img" aria-label="Photo of children gathered around a birthday cake with candles and a wrapped present"></div>
  <h2 class="abs how">HOW IT WORKS</h2>

  <svg class="abs steps-icons" viewBox="0 0 538 70" aria-hidden="true">
    <!-- envelope screens -->
    <g fill="#fff" stroke="#e6007e" stroke-width="2">
      <rect x="52" y="16" width="72" height="40" rx="3"/>
      <rect x="88" y="4" width="26" height="18" rx="2"/>
      <rect x="118" y="14" width="22" height="16" rx="2"/>
    </g>
    <rect x="46" y="56" width="84" height="5" fill="#e6007e"/>
    <g fill="#6cc13a">
      <rect x="70" y="26" width="36" height="22"/>
    </g>
    <path d="M70 26l18 12 18-12" stroke="#fff" stroke-width="2" fill="none"/>
    <!-- arrows -->
    <path d="M168 30l16 6-16 6 4-6z" fill="#8a1230"/>
    <path d="M330 30l16 6-16 6 4-6z" fill="#8a1230"/>
    <!-- dollar -->
    <path d="M213 36a28 28 0 0 1 56 0z" fill="#e6007e"/>
    <path d="M213 36a28 28 0 0 0 56 0z" fill="#6cc13a"/>
    <text x="241" y="47" text-anchor="middle" font-family="Open Sans, sans-serif" font-weight="700" font-size="30" fill="#fff">$</text>
    <!-- heart + box -->
    <circle cx="384" cy="36" r="25" fill="#fff" stroke="#e6007e" stroke-width="2"/>
    <path d="M384 48c-14-9-16-16-12-21 4-4 9-2 12 2 3-4 8-6 12-2 4 5 2 12-12 21z" fill="#6cc13a"/>
    <text x="420" y="43" text-anchor="middle" font-family="Open Sans, sans-serif" font-weight="800" font-size="20" fill="#8a1230">+</text>
    <circle cx="456" cy="36" r="25" fill="#fff" stroke="#e6007e" stroke-width="2"/>
    <rect x="445" y="27" width="22" height="20" fill="#e6007e"/>
  </svg>

  <div class="abs how-col how-col--1"><ul><li>Send online invitations Cards</li></ul></div>
  <div class="abs how-col how-col--2"><ul><li>Guests RSVP and contribute money online</li><li>Contributions raised are split into two sums.</li></ul></div>
  <div class="abs how-col how-col--3"><ul><li>The first is sent to a charity you choose</li><li>The second is yours to buy something special with</li></ul></div>

  <div class="abs steps-box">
    <ol class="steps">
      <li><b>STEP 1 :</b><span>Choose your invitation and charity</span></li>
      <li><b>STEP 2 :</b><span>Enter your party details and the gift you are saving for</span></li>
      <li><b>STEP 3 :</b><span>Send your invitations to your guests</span></li>
      <li><b>STEP 4 :</b><span>Your guests RSVP and contribute</span></li>
      <li><b>STEP 5 :</b><span>View party summary and track the RSVPs, contributions</span></li>
      <li><b>STEP 6 :</b><span>Send you guests thank you cards and inform them of the meaningful funds they have raised!</span></li>
    </ol>
    <p class="steps-cta">SIMPLE, SMART AND BETTER!</p>
  </div>
  <div class="abs steps-tab">SIX EASY STEPS</div>

  <div class="abs brand back-brand">
    <span class="brand__mark"></span>
    <span class="brand__name">bramblecast</span>
  </div>
  <p class="abs footer">Visit <b>www.bramblecast-invites.example</b> to set up your party <span class="divider"></span><span class="social"></span>search ‘<b>bramblecast</b>’</p>
</section>

</body>
</html>
```